Gentleman's grooming products require a business card

I need a business card that incorporates the logo [ or parts of ] that we had Pixel Hive design for us as uploaded.

We sell online, mens grooming products including moustache waxes, beard oils and shaving accessories.
We want a card that is classy, professional and a card that shouts mens products.

Target Market(s)

Young professional male market

Industry/Entity Type

Business

Contact Information for Business Card

Ross and Edith Carwell
Lather and Lore
Suppliers of gentleman's waxes, oils and shaving essentials
M :0418529647
E : ross@latherandlore.com.au
E : edith@latherandlore.com.au
E : sales@theblokesbalmery.com.au

W : www.latherandlore.com.au

Requirements
Must have
• Class
Nice to have
• Professionalism

```html
<!DOCTYPE html>
<html lang="en">
<head>
<meta charset="utf-8">
<title>Lather and Lore — Business Card</title>
<link rel="stylesheet" href="https://fonts.googleapis.com/css2?family=Source+Sans+3:ital,wght@0,400;0,600;1,400&display=swap">
<style>
  :root {
    --backdrop: #3b3b3b;
    --card: #050505;
    --ink: #ececec;
    --ink-soft: #d4d4d4;
    --rule: #e0e0e0;
  }
  * { margin: 0; padding: 0; box-sizing: border-box; }
  html, body {
    width: 1105px;
    height: 1200px;
    overflow: hidden;
    background: var(--backdrop);
    font-family: "Source Sans 3", "Myriad Pro", Arial, sans-serif;
    color: var(--ink);
  }
  .card {
    position: absolute;
    left: 196px;
    width: 720px;
    height: 410px;
    background: var(--card);
  }
  .card--front { top: 146px; }
  .card--back { top: 602px; }

  /* Front: brand lockup */
  .brand {
    position: absolute;
    left: 46px;
    top: 130px;
    width: 294px;
    text-align: center;
  }
  .brand__mark {
    display: block;
    width: 48px;
    height: 48px;
    margin: 0 auto 14px;
    border: 2px solid var(--ink);
  }
  .brand__rule {
    height: 0;
    border-top: 1.5px solid var(--rule);
  }
  .brand__name {
    font-size: 34px;
    font-weight: 400;
    line-height: 1;
    padding: 10px 0 6px;
    letter-spacing: 0.5px;
  }
  .brand__tagline {
    font-size: 8.5px;
    letter-spacing: 0.6px;
    text-transform: uppercase;
    padding-bottom: 3px;
    white-space: nowrap;
  }

  /* Front: contact block */
  .contact {
    position: absolute;
    left: 372px;
    top: 88px;
    width: 300px;
  }
  .contact__name {
    font-size: 26px;
    font-weight: 600;
    line-height: 1;
  }
  .contact__phone {
    font-size: 18px;
    margin-top: 10px;
    line-height: 1;
  }
  .contact__phone b { font-weight: 600; }
  .contact__divider {
    height: 0;
    width: 294px;
    border-top: 2.5px dotted var(--rule);
    margin: 14px 0 16px;
  }
  .contact__line {
    font-size: 19px;
    line-height: 29px;
    color: var(--ink-soft);
  }

  /* Back */
  .emblem {
    position: absolute;
    left: 0;
    right: 0;
    top: 92px;
    text-align: center;
  }
  .emblem__mark {
    display: block;
    width: 64px;
    height: 64px;
    margin: 0 auto 22px;
    border: 3px solid var(--ink);
  }
  .emblem__name {
    font-size: 40px;
    font-weight: 400;
    line-height: 1;
    letter-spacing: 0.5px;
  }
  .slogan {
    position: absolute;
    left: 0;
    right: 0;
    top: 326px;
    text-align: center;
    font-size: 18px;
    font-style: italic;
    line-height: 25px;
  }
</style>
</head>
<body>
  <section class="card card--front">
    <div class="brand">
      <span class="brand__mark"></span>
      <div class="brand__rule"></div>
      <div class="brand__name">Lather and Lore</div>
      <div class="brand__tagline">Suppliers of gentlemen's waxes, oils and shaving essentials</div>
      <div class="brand__rule"></div>
    </div>
    <div class="contact">
      <div class="contact__name">Ross &amp; Edith Carwell</div>
      <div class="contact__phone"><b>M :</b> 0418529647</div>
      <div class="contact__divider"></div>
      <div class="contact__line">ross@latherandlore.com.au</div>
      <div class="contact__line">edith@latherandlore.com.au</div>
      <div class="contact__divider"></div>
      <div class="contact__line">sales@theblokesbalmery.com.au</div>
      <div class="contact__line">www.latherandlore.com.au</div>
    </div>
  </section>

  <section class="card card--back">
    <div class="emblem">
      <span class="emblem__mark"></span>
      <div class="emblem__name">Lather and Lore</div>
    </div>
    <p class="slogan">Suppliers of gentleman's<br>waxes, oils &amp; shaving essentials</p>
  </section>
</body>
</html>
```